Flyer in Creole

Instructions for Designer
Objective: Create two versions of the flyer for Densora dental services: one in French and one in Creole. Target audience is elders of the haitian community in Montreal so include picture of an older person with a darker skin complexion.

I have included our original flyer.

Densora - Sèvis Dantè pou Granmoun Aje
Nou ofri swen dantè san frè pou moun 65 an e plis!

La Clinique Dentaire Densora gen kè kontan patisipe nan Pwogram Sourir Nasyonal (PSNB). Si w gen 65 an oubyen plis, ou ka resevwa swen dantè gratis, san frè siplemantè si w kalifye.

Kijan pou Kalifye?

Si w gen 65 an ou plis, ou ka jwenn tretman dantè san frè.
Vizite: https://www.plansourir-exemple.org/aplike/fomile.html pou w aplike epi w konnen si w kalifye.
Sèvis Nou Ofri:

Netwayaj dantè: Sante bouch ou enpòtan, fè yon netwayaj pwofesyonèl pou prezève sante dantè w.
Egzamen ak radyografi: Pran yon randevou pou yon egzamen konplè ak radyografi.
Ekstraksyon dantè: Retire dan ki domaje oswa ki fè w mal.
Ijans dantè: Tretman rapid pou doulè, dan kase, oswa lòt ijans.
Pwotèz dantè konplè ak pasyèl: Nou ranplase dan ki manke yo pou yon bèl souri ak bon sante.
Rele Kounye a pou Fiks yon Randevou: 514-555-0187
Klinik Densora - 2860 Rue Belmarais E, 2yèm etaj, Montreal, QC H2X 3K9
Design Elements:
Use images that resonate with the Creole-speaking community.
Ensure the text is clear and accessible.

```html
<!DOCTYPE html>
<html lang="ht">
<head>
<meta charset="utf-8">
<title>Densora – Sèvis Dantè pou Granmoun Aje</title>
<link rel="stylesheet" href="https://fonts.googleapis.com/css2?family=Fraunces:opsz,wght@9..144,500;9..144,600&family=Inter:wght@300;400;600&display=swap">
<style>
  :root{
    --navy:#243450;
    --navy-deep:#1d2b44;
    --sky:#a9c8f2;
    --sky-soft:#c7dbf7;
    --ink:#2b3a56;
    --paper:#ffffff;
    --backdrop:#e3e3e3;
    --head-text:#eef2fb;
  }
  *{margin:0;padding:0;box-sizing:border-box}
  html,body{width:1200px;height:2173px;overflow:hidden;background:var(--backdrop)}
  .flyer{position:absolute;left:40px;top:362px;width:1120px;height:1449px;background:var(--paper);overflow:hidden;color:var(--ink);font-family:"Inter",sans-serif}
  .abs{position:absolute}
  .serif{font-family:"Fraunces",serif}
  .center{left:0;width:100%;text-align:center}

  .hero-art{left:0;top:0}
  .brand{top:30px;font-size:86px;font-weight:500;color:var(--navy);letter-spacing:1px;line-height:1}
  .title{top:186px;font-size:82px;font-weight:600;line-height:76px;color:var(--head-text)}
  .subtitle{top:347px;font-size:35px;font-weight:500;color:var(--head-text)}
  .intro{top:396px;font-size:24px;font-weight:300;line-height:28px;color:var(--head-text)}

  .pill{background:var(--sky);border-radius:26px;color:var(--navy);font-family:"Fraunces",serif;font-weight:500;text-align:center}
  .pill-qualify{left:356px;top:516px;width:438px;height:50px;font-size:33px;line-height:50px}
  .qualify-text{top:586px;font-size:24px;line-height:29.5px;color:var(--navy-deep)}
  .qualify-text b{font-weight:600}

  .photo{top:696px;width:312px;height:164px;border:3px solid var(--navy);border-radius:10px}
  .photo-1{left:80px;background:linear-gradient(120deg,#c9a38a,#e9e4e0 55%,#b7c9d8)}
  .photo-2{left:403px;background:linear-gradient(110deg,#8e9aa6,#c98a58 50%,#d8dde2)}
  .photo-3{left:727px;background:linear-gradient(120deg,#6fa2b0,#d9d4d0 50%,#6e6fb3)}

  .services-box{left:80px;top:912px;width:960px;height:367px;border:3px solid var(--sky-soft);border-radius:16px}
  .pill-services{left:125px;top:886px;width:868px;height:52px;font-size:33px;line-height:52px}
  .service{position:absolute;width:350px}
  .service .icon{position:absolute;left:-62px;top:-7px;width:46px;height:46px}
  .service h3{font-family:"Fraunces",serif;font-weight:500;font-size:29px;line-height:32px;color:var(--navy)}
  .service p{font-size:20px;font-weight:300;line-height:23px;margin-top:6px;width:335px}
  .svc-clean{left:194px;top:966px}
  .svc-exam{left:194px;top:1086px}
  .svc-extract{left:194px;top:1188px}
  .svc-emergency{left:663px;top:966px}
  .svc-denture{left:663px;top:1086px}

  .footer{left:0;top:1306px;width:1120px;height:143px;background:var(--navy)}
  .cta{left:80px;top:1333px;font-size:29px;font-weight:500;color:var(--sky)}
  .address{left:80px;top:1372px;width:531px;height:31px;border:1.5px solid var(--head-text);border-radius:16px;color:var(--head-text);font-size:15px;line-height:28px;text-align:center}
  .phone-icon{left:632px;top:1353px}
  .phone{left:692px;top:1342px;font-size:55px;font-weight:500;color:var(--sky);line-height:1;white-space:nowrap}
</style>
</head>
<body>
<main class="flyer">
  <svg class="abs hero-art" width="1120" height="560" viewBox="0 0 1120 560">
    <defs>
      <linearGradient id="heroTone" x1="0" y1="0" x2="1" y2="1">
        <stop offset="0" stop-color="#26324a"/>
        <stop offset="0.5" stop-color="#3b4b66"/>
        <stop offset="1" stop-color="#2a3a55"/>
      </linearGradient>
    </defs>
    <path d="M0 450 Q560 560 1120 450 L1120 466 Q560 578 0 466 Z" fill="var(--sky)"/>
    <path role="img" aria-label="Dental clinic scene with a smiling older patient and a dentist" d="M0 0 H1120 V440 Q560 548 0 440 Z" fill="url(#heroTone)"/>
    <path d="M293 0 H827 Q800 158 560 158 Q320 158 293 0 Z" fill="var(--paper)"/>
  </svg>

  <div class="abs center serif brand">densora</div>
  <h1 class="abs center serif title">Sèvis Dantè pou<br>Granmoun Aje</h1>
  <p class="abs center serif subtitle">Nou ofri swen dantè san frè pou moun 65 an e plis!</p>
  <p class="abs center intro">La Clinique Dentaire Densora gen kè kontan patisipe nan Pwogram<br>Sourir Nasyonal (PSNB). Si w gen 65 an oubyen plis, ou ka resevwa<br>swen dantè gratis, san frè siplemantè si w kalifye.</p>

  <h2 class="abs pill pill-qualify">Kijan pou Kalifye?</h2>
  <p class="abs center qualify-text"><b>Si w gen 65 an ou plis, ou ka jwenn tretman dantè san frè. Vizite:</b><br>https://www.plansourir-exemple.org/aplike/fomile.html<br><b>pou w aplike epi w konnen si w kalifye.</b></p>

  <div class="abs photo photo-1" role="img" aria-label="Smiling older woman in a dental chair with a dentist"></div>
  <div class="abs photo photo-2" role="img" aria-label="Dentist showing a denture model to an older patient"></div>
  <div class="abs photo photo-3" role="img" aria-label="Older man receiving a dental checkup"></div>

  <div class="abs services-box"></div>
  <h2 class="abs pill pill-services">Sèvis Nou Ofri:</h2>

  <div class="service svc-clean">
    <svg class="icon" viewBox="0 0 46 46"><circle cx="23" cy="23" r="22" fill="var(--navy)"/><path d="M15 17c0-4 4-5 8-3 4-2 8-1 8 3 0 4-2 6-2 10s-2 7-3 7-1-6-3-6-2 6-3 6-3-3-3-7-2-6-2-10z" fill="none" stroke="#fff" stroke-width="2"/></svg>
    <h3>Netwayaj dantè:</h3>
    <p>Sante bouch ou enpòtan, fè yon netwayaj pwofesyonèl pou prezève sante dantè w.</p>
  </div>
  <div class="service svc-exam">
    <svg class="icon" viewBox="0 0 46 46"><circle cx="23" cy="23" r="22" fill="var(--navy)"/><circle cx="21" cy="20" r="8" fill="none" stroke="#fff" stroke-width="2"/><path d="M27 26l7 7" stroke="#fff" stroke-width="2.5"/></svg>
    <h3>Egzamen ak radyografi:</h3>
    <p>Pran yon randevou pou yon egzamen konplè ak radyografi.</p>
  </div>
  <div class="service svc-extract">
    <svg class="icon" viewBox="0 0 46 46"><circle cx="23" cy="23" r="22" fill="var(--navy)"/><path d="M16 20c0-4 4-5 7-3 3-2 7-1 7 3 0 4-2 5-2 9s-2 6-3 6-1-5-2-5-1 5-2 5-3-2-3-6-2-5-2-9z" fill="none" stroke="#fff" stroke-width="2"/><path d="M23 6v8M19 10l4 4 4-4" fill="none" stroke="#fff" stroke-width="2"/></svg>
    <h3>Ekstraksyon dantè:</h3>
    <p>Retire dan ki domaje oswa ki fè w mal.</p>
  </div>
  <div class="service svc-emergency">
    <svg class="icon" viewBox="0 0 46 46"><circle cx="23" cy="23" r="22" fill="var(--navy)"/><path d="M15 17c0-4 4-5 8-3 4-2 8-1 8 3 0 4-2 6-2 10s-2 7-3 7-1-6-3-6-2 6-3 6-3-3-3-7-2-6-2-10z" fill="none" stroke="#fff" stroke-width="2"/><path d="M23 16l-2 6h4l-2 6" fill="none" stroke="#fff" stroke-width="1.8"/></svg>
    <h3>Ijans dantè:</h3>
    <p>Tretman rapid pou doulè, dan kase, oswa lòt ijans.</p>
  </div>
  <div class="service svc-denture">
    <svg class="icon" viewBox="0 0 46 46"><circle cx="23" cy="23" r="22" fill="var(--navy)"/><path d="M13 30V20c0-6 20-6 20 0v10" fill="none" stroke="#fff" stroke-width="2"/><path d="M18 30V22M23 30V21M28 30V22" stroke="#fff" stroke-width="2"/></svg>
    <h3>Pwotèz dantè konplè<br>ak pasyèl:</h3>
    <p>Nou ranplase dan ki manke yo pou yon bèl souri ak bon sante.</p>
  </div>

  <div class="abs footer"></div>
  <p class="abs serif cta">Rele Kounye a pou Fiks yon Randevou:</p>
  <p class="abs address">Klinik Densora - 2860 Rue Belmarais E, 2yèm etaj, Montreal, QC H2X 3K9</p>
  <svg class="abs phone-icon" width="48" height="48" viewBox="0 0 48 48"><circle cx="24" cy="24" r="21" fill="none" stroke="var(--sky)" stroke-width="3"/><path d="M17 14c2-1 3 0 4 2l1 3c0 1-1 2-2 3 1 3 3 5 6 6 1-1 2-2 3-2l3 1c2 1 3 2 2 4-1 2-3 3-5 3-8-1-14-7-15-15 0-2 1-4 3-5z" fill="var(--sky)"/></svg>
  <p class="abs serif phone">514-555-0187</p>
</main>
</body>
</html>
```